Brightwell Letterhead

We would like a letterhead for our company. I have uploaded our logo.

Brightwell Peak Consulting
1450 W Corvin Rd Ste 310
Fairmont Springs, TX 75482
844-555-0172

```html
<!DOCTYPE html>
<html lang="en">
<head>
<meta charset="utf-8">
<title>Brightwell Letterhead</title>
<link rel="stylesheet" href="https://fonts.googleapis.com/css2?family=Arimo:ital,wght@0,400;0,700;1,400&family=Jost:wght@500;600&display=swap">
<style>
  :root {
    --backdrop: #2b2721;
    --paper: #ffffff;
    --brand-blue: #3d6e86;
    --brand-green: #95c4a2;
    --ink: #333333;
    --footer-ink: #ffffff;
  }
  * { margin: 0; padding: 0; box-sizing: border-box; }
  html, body { width: 1200px; height: 1200px; overflow: hidden; background: var(--backdrop); }
  .canvas { position: relative; width: 1200px; height: 1200px; }
  .letterhead {
    position: absolute; left: 160px; top: 30px; width: 880px; height: 1140px;
    background: var(--paper); overflow: hidden;
    font-family: "Arimo", Arial, sans-serif; color: var(--ink);
  }
  .corner-accent {
    position: absolute; left: 0; top: 0; width: 279px; height: 290px;
    border-bottom-right-radius: 100%;
    background: linear-gradient(135deg, var(--brand-blue) 0%, var(--brand-green) 100%);
    opacity: 0.9;
  }
  .brand {
    position: absolute; left: 535px; top: 48px;
    display: flex; align-items: center; gap: 12px;
  }
  .brand-dot { width: 36px; height: 36px; border-radius: 50%; background: var(--brand-green); }
  .brand-name {
    font-family: "Jost", "Futura", sans-serif; font-weight: 600; color: var(--brand-blue);
    font-size: 21px; letter-spacing: 2.5px; line-height: 22px; text-transform: uppercase;
  }
  .letter { position: absolute; left: 145px; width: 628px; font-size: 16.8px; }
  .date { top: 296px; font-weight: 700; }
  .recipient { top: 356px; line-height: 20px; }
  .recipient .name { font-weight: 700; font-size: 17px; }
  .recipient .title { font-style: italic; }
  .body { top: 466px; line-height: 21.3px; }
  .body p { text-align: justify; margin-bottom: 17px; }
  .closing { top: 902px; text-align: right; }
  .signature {
    display: block; margin: 10px 10px 0 auto; width: 118px; height: 38px;
    background: linear-gradient(90deg, #eeeeee, #f6f6f6); border-radius: 4px;
  }
  .closing .signer { display: block; font-weight: 700; font-size: 17px; margin: 2px 10px 0 0; }
  .footer {
    position: absolute; left: 0; bottom: 0; width: 100%; height: 58px;
    background: var(--brand-blue); color: var(--footer-ink);
    font-family: "Jost", "Futura", sans-serif; font-weight: 500; font-size: 14px;
    display: flex; align-items: center; justify-content: center; gap: 10px; letter-spacing: 0.2px;
    white-space: nowrap;
  }
  .footer .company { font-weight: 600; text-transform: uppercase; }
  .footer .item { display: flex; align-items: center; gap: 6px; }
  .footer svg { width: 16px; height: 16px; flex: none; }
</style>
</head>
<body>
<div class="canvas">
  <article class="letterhead">
    <div class="corner-accent" role="img" aria-label="Brand colour accent in blue and green"></div>

    <header class="brand">
      <span class="brand-dot"></span>
      <div class="brand-name">Brightwell Peak<br>Consulting</div>
    </header>

    <p class="letter date">Date, 22 February 2022</p>

    <div class="letter recipient">
      <p>To:</p>
      <p class="name">Daniel Hart</p>
      <p class="title">Chief Officer</p>
    </div>

    <div class="letter body">
      <p>Lorem ipsum dolor sit amet, consectetur adipiscing elit. Duis auctor sem vel metus interdum porta. Duis consequat bibendum felis eget cursus. Nulla eget purus vehicula ipsum finibus egestas. Nullam ligula ipsum, mollis sed gravida vitae, maximus eu dolor. Morbi luctus sem a congue consectetur. uis consequat bibendum felis eget cursus. Nulla eget purus vehicula ipsum finibus egestas. Nullam ligula ipsum, mollis sed gravida vitae, maximus eu dolor. Morbi luctus sem a congue consectetur.</p>
      <p>Orci varius natoque penatibus et magnis dis parturient montes, nascetur ridiculus mus. Vestibulum congue eros auctor, ullamcorper libero blandit, tempor tellus. Proin vitae tellus et nunc fringilla lacinia. Sed augue erat, facilisis laoreet velit a, convallis mattis nunc. Nunc sagittis ligula vitae sollicitudin sollicitudin. Ullamcorper libero blandit, tempor tellus. Proin vitae tellus et nunc fringilla lacinia. Sed augue erat, facilisis laoreet velit a, convallis mattis nunc. Nunc sagittis ligula vitae sollicitudin sollicitudin.</p>
      <p>Nulla facilisi. Nulla quis odio vitae purus aliquam fermentum ut nec diam. Fusce sed velit ultrices, aliquam augue ut, sollicitudin orci.</p>
    </div>

    <div class="letter closing">
      <span>Kind Regards</span>
      <span class="signature" role="img" aria-label="Handwritten signature"></span>
      <span class="signer">Daniel Hart</span>
    </div>

    <footer class="footer">
      <span class="company">Brightwell Peak Consulting</span>
      <span>|</span>
      <span class="item">
        <svg viewBox="0 0 16 16" aria-hidden="true"><circle cx="8" cy="8" r="7" fill="none" stroke="var(--brand-green)" stroke-width="1.4"/><path d="M8 3.8a2.6 2.6 0 0 0-2.6 2.6C5.4 8.4 8 11.8 8 11.8s2.6-3.4 2.6-5.4A2.6 2.6 0 0 0 8 3.8z" fill="none" stroke="var(--brand-green)" stroke-width="1.3"/><circle cx="8" cy="6.4" r="0.9" fill="var(--brand-green)"/></svg>
        1450 W Corvin Rd Ste 310 Fairmont Springs, TX 75482
      </span>
      <span>|</span>
      <span class="item">
        <svg viewBox="0 0 16 16" aria-hidden="true"><circle cx="8" cy="8" r="7" fill="none" stroke="var(--brand-green)" stroke-width="1.4"/><path d="M5.6 4.6l1.3-.3.8 1.9-.9.7a5 5 0 0 0 2.3 2.3l.7-.9 1.9.8-.3 1.3c-3.1.3-6.1-2.7-5.8-5.8z" fill="var(--brand-green)"/></svg>
        844-555-0172
      </span>
    </footer>
  </article>
</div>
</body>
</html>
```